Wakeboarding and Aqua Park front cover for flyer

I would like a front cover that I can use on a DL flyer to advertise both our Aqua Park and Cable Ski. The design should reflect the fun nature of our activity and appeal to both families and young people (18-30) but with may be a touch of an extreme sports feel.

I would like two pictures to be visible, one of the Aqua Park and the other the cable ski plus our logo. Both should have prominence but if the design has one at the top and the other at the bottom please put the Aqua Park at the top as this is currently our most popular activity.

There should be some text visible near the Aqua Park picture saying:

AQUA PARK
"Bigger and Better for 2017!"

There should be some text visible near/over the Cable Ski picture saying:

CABLE SKI
"Try kneeboarding, water skiing or wakeboarding this summer!"

Target Market(s)

Young people, families

Industry/Entity Type

Entertainment

Colors
0255a3
fbed22
fbee3e
0692cd

Requirements
Must have
• Picture of wakeboarding, picture of Aqua Park
Nice to have
• nice vibrant blues and yellows. illustration.
Should not have
• Have included a few extra aqua park images now in case they look better than the first one uploaded. Don't need to include them all though.

```html
<!DOCTYPE html>
<html lang="en">
<head>
<meta charset="utf-8">
<title>Ridgeway Cable Waterski – DL Flyer Cover</title>
<link rel="stylesheet" href="https://fonts.googleapis.com/css2?family=Exo+2:wght@600;700;800&family=Roboto+Condensed:wght@700&display=swap">
<style>
  :root {
    --page-bg: #e9ecef;
    --deep-blue: #0b2f6e;
    --brand-blue: #0255a3;
    --sky-blue: #0692cd;
    --navy: #0d1f5c;
    --sun-yellow: #fbed22;
    --pale-yellow: #fbee3e;
    --gold: #c9911f;
    --white: #ffffff;
  }
  * { margin: 0; padding: 0; box-sizing: border-box; }
  html, body {
    width: 902px; height: 1200px; overflow: hidden;
    background: var(--page-bg);
  }
  .flyer {
    position: absolute; left: 171px; top: 25px;
    width: 560px; height: 1150px; overflow: hidden;
    box-shadow: 0 6px 24px rgba(0,0,0,.25);
  }
  .flyer__art { position: absolute; inset: 0; }
  .brand {
    position: absolute; top: 40px; left: 0; width: 100%;
    display: flex; justify-content: center; align-items: center; gap: 12px;
    font-family: "Exo 2", sans-serif; font-weight: 800;
    font-size: 30px; line-height: 1; color: var(--white);
    text-transform: lowercase; letter-spacing: .5px;
  }
  .brand__mark { width: 26px; height: 26px; border-radius: 50%; background: var(--white); }
  .headline {
    position: absolute; top: 532px; left: 0; width: 100%;
    text-align: center;
    font-family: "Exo 2", sans-serif; font-weight: 700;
    font-size: 38px; line-height: 52px; color: var(--navy);
    letter-spacing: 1px;
  }
  .offer {
    position: absolute; top: 966px; left: 0; width: 100%;
    text-align: center;
    font-family: "Exo 2", sans-serif; font-weight: 700;
    font-size: 24px; line-height: 32px; color: var(--sun-yellow);
  }
  .offer__last { color: var(--white); }
  .contact {
    position: absolute; top: 1100px; left: 0; width: 100%;
    display: flex; justify-content: center; align-items: center; gap: 10px;
    font-family: "Roboto Condensed", sans-serif; font-weight: 700;
    font-size: 26px; color: var(--navy);
  }
  .contact__label { color: var(--brand-blue); }
  .contact__icon { width: 22px; height: 22px; }
</style>
</head>
<body>
<main class="flyer">
  <svg class="flyer__art" width="560" height="1150" viewBox="0 0 560 1150" aria-hidden="false">
    <defs>
      <linearGradient id="topBlue" x1="0" y1="0" x2="0" y2="1">
        <stop offset="0" stop-color="#0a3a85"/>
        <stop offset=".5" stop-color="#0255a3"/>
        <stop offset="1" stop-color="#0692cd"/>
      </linearGradient>
      <radialGradient id="sunBurst" cx=".5" cy=".75" r=".7">
        <stop offset="0" stop-color="#fbee3e"/>
        <stop offset=".6" stop-color="#fbed22"/>
        <stop offset="1" stop-color="#f2c814"/>
      </radialGradient>
      <linearGradient id="bandBlue" x1="0" y1="0" x2="1" y2="0">
        <stop offset="0" stop-color="#0b2f6e"/>
        <stop offset=".5" stop-color="#0255a3"/>
        <stop offset="1" stop-color="#0b2f6e"/>
      </linearGradient>
      <linearGradient id="parkPhoto" x1="0" y1="0" x2="0" y2="1">
        <stop offset="0" stop-color="#4d86c4"/>
        <stop offset=".45" stop-color="#b9d2ea"/>
        <stop offset=".62" stop-color="#4a6a4e"/>
        <stop offset=".7" stop-color="#3f5a6e"/>
        <stop offset="1" stop-color="#26394a"/>
      </linearGradient>
      <linearGradient id="skiPhoto" x1="0" y1="0" x2="0" y2="1">
        <stop offset="0" stop-color="#7a9fc0"/>
        <stop offset=".25" stop-color="#4f7a3c"/>
        <stop offset=".5" stop-color="#6a8a7a"/>
        <stop offset=".65" stop-color="#b8c6d2"/>
        <stop offset="1" stop-color="#8ea1b3"/>
      </linearGradient>
    </defs>

    <!-- top blue field -->
    <rect class="top-field" x="0" y="0" width="560" height="560" fill="url(#topBlue)"/>
    <!-- yellow sunburst band -->
    <path class="sun-band" d="M0,330 Q280,470 560,330 L560,680 L0,680 Z" fill="url(#sunBurst)"/>

    <!-- gold swoosh behind oval -->
    <ellipse class="swoosh" cx="290" cy="322" rx="286" ry="186" fill="none" stroke="var(--gold)" stroke-width="10"/>
    <ellipse cx="282" cy="326" rx="280" ry="184" fill="none" stroke="var(--white)" stroke-width="6"/>
    <ellipse cx="282" cy="326" rx="274" ry="178" fill="none" stroke="var(--navy)" stroke-width="6"/>
    <ellipse cx="282" cy="326" rx="268" ry="172" fill="var(--white)"/>
    <ellipse class="photo photo--aqua-park" cx="282" cy="326" rx="262" ry="166" fill="url(#parkPhoto)"
             role="img" aria-label="Photo of the inflatable aqua park on the lake with a climbing tower and slide"/>

    <!-- cable ski photo -->
    <rect class="photo photo--cable-ski" x="0" y="640" width="560" height="312" fill="url(#skiPhoto)"
          role="img" aria-label="Photo of a young rider wakeboarding on the cable lake, spraying water"/>
    <path d="M0,680 L0,640 L560,640 L560,680 Q280,630 0,680 Z" fill="var(--sun-yellow)"/>
    <path d="M0,680 Q280,630 560,680" fill="none" stroke="var(--gold)" stroke-width="4"/>

    <!-- offer band -->
    <rect class="offer-band" x="0" y="950" width="560" height="140" fill="url(#bandBlue)"/>
    <!-- contact strip -->
    <path class="contact-strip" d="M0,1082 Q280,1050 560,1082 L560,1150 L0,1150 Z" fill="var(--sun-yellow)"/>
  </svg>

  <div class="brand"><span class="brand__mark"></span><span class="brand__name">ridgeway cable waterski</span></div>

  <h1 class="headline">BIGGER AND BETTER<br>FOR 2017!</h1>

  <p class="offer">TRY KNEEBOARDING, WATER<br>SKIING OR WAKEBOARDING<br><span class="offer__last">THIS SUMMER!</span></p>

  <p class="contact">
    <span class="contact__label">Call Us</span>
    <svg class="contact__icon" viewBox="0 0 24 24" aria-hidden="true">
      <circle cx="12" cy="12" r="10.5" fill="none" stroke="var(--navy)" stroke-width="2"/>
      <path d="M8.5 6.5l2 2.2-1 1.6c.8 1.7 2 2.9 3.7 3.7l1.6-1 2.2 2-1.2 1.8c-3.8-.4-8.3-4.9-8.7-8.7z" fill="var(--navy)"/>
    </svg>
    <span class="contact__number">0123 456 7890</span>
  </p>
</main>
</body>
</html>
```